Crestline Gas and Plumbing Business Card Design

I am after a business card design for my plumbing business called 'Crestline Gas & Plumbing'. I do all types of plumbing and gas work and specialise in general maintenance plumbing. Would like to see designs using current logo

Industry/Entity Type

Plumbing

Contact Information for Business Card

Name - Dale Whitcombe
Phone number - 0455163027
Email - admin@crestlinegasandplumbing.example.com.au
ABN - 68204915336

```html
<!DOCTYPE html>
<html lang="en">
<head>
<meta charset="utf-8">
<title>Crestline Gas &amp; Plumbing – Business Cards</title>
<link rel="stylesheet" href="https://fonts.googleapis.com/css2?family=Didact+Gothic&display=swap">
<style>
  :root {
    --backdrop: #1c1c1c;
    --card: #ffffff;
    --brand-blue: #1f5fc4;
    --accent-orange: #f28a1a;
    --ink: #1a1a1a;
    --rule: #333333;
    --faint-grey: #ececec;
    --faint-warm: #fbeede;
  }
  * { box-sizing: border-box; margin: 0; padding: 0; }
  html, body {
    width: 1200px; height: 1200px; overflow: hidden;
    background: var(--backdrop);
    font-family: "Didact Gothic", "Century Gothic", sans-serif;
  }
  .canvas { position: relative; width: 1200px; height: 1200px; }
  .card {
    position: absolute; left: 180px; width: 840px; height: 500px;
    background: var(--card); border-radius: 28px; overflow: hidden;
  }
  .card--front { top: 70px; }
  .card--back { top: 630px; }

  .brand { display: flex; align-items: center; gap: 14px; color: var(--brand-blue); }
  .brand__dot { border-radius: 50%; background: var(--brand-blue); flex: none; }
  .brand__name { line-height: 1.1; }

  .card--front .brand {
    position: absolute; left: 90px; top: 150px;
  }
  .card--front .brand__dot { width: 54px; height: 54px; }
  .card--front .brand__name { font-size: 44px; }

  .watermark {
    position: absolute; display: flex; align-items: center; gap: 18px;
  }
  .watermark__dot { width: 180px; height: 180px; border-radius: 50%; background: var(--faint-grey); }
  .watermark__name { font-size: 30px; color: var(--faint-warm); max-width: 200px; line-height: 1.15; }
  .card--front .watermark { right: 40px; bottom: 30px; }
  .card--back .watermark { right: 40px; bottom: 30px; }

  .card--back .brand { position: absolute; left: 48px; top: 40px; }
  .card--back .brand__dot { width: 34px; height: 34px; }
  .card--back .brand__name { font-size: 26px; }

  .contact { position: absolute; left: 60px; top: 110px; color: var(--ink); }
  .contact__name { font-size: 28px; color: var(--accent-orange); letter-spacing: 0.5px; }
  .contact__title {
    display: inline-block; font-size: 24px; margin-top: 4px; padding-bottom: 6px;
    border-bottom: 2px solid var(--rule); padding-right: 20px;
  }
  .contact__list { list-style: none; margin-top: 18px; font-size: 17px; line-height: 1.6; }
  .contact__list li { display: flex; }
  .contact__label { width: 80px; }
  .contact__address { margin-top: 10px; font-size: 17px; line-height: 1.5; }
</style>
</head>
<body>
<main class="canvas">
  <section class="card card--front" aria-label="Card front">
    <div class="brand">
      <span class="brand__dot"></span>
      <span class="brand__name">Crestline Gas &amp; Plumbing</span>
    </div>
    <div class="watermark" role="img" aria-label="Faint brand mark decoration">
      <span class="watermark__dot"></span>
    </div>
  </section>

  <section class="card card--back" aria-label="Card back">
    <div class="brand">
      <span class="brand__dot"></span>
      <span class="brand__name">Crestline Gas &amp; Plumbing</span>
    </div>
    <div class="contact">
      <p class="contact__name">DALE WHITCOMBE</p>
      <p class="contact__title">Your Title</p>
      <ul class="contact__list">
        <li><span class="contact__label">Phone</span>: 0455163027</li>
        <li><span class="contact__label">E-mail</span>: admin@crestlinegasandplumbing.example.com.au</li>
        <li><span class="contact__label">ABN</span>: 68204915336</li>
      </ul>
      <p class="contact__address">1180 Harbour View Rd Ste 200<br>Your City, 40218</p>
    </div>
    <div class="watermark" role="img" aria-label="Faint brand mark decoration">
      <span class="watermark__dot"></span>
    </div>
  </section>
</main>
</body>
</html>
```